Pelton|Marsh & Quillan business card contest

We need a logo for an upscale boutique diversified company involved in real estate, investments, cattle, and more. Our businesses DO NOT need to be reflected in the business card nor do we want them noted. This is our logo and colors and we love our logo and colors. Our logo looks best against a black background and we like to include the firm name in our logo usage. importantly, the names Pelton and Marsh are separated by | not / and we use an ampersand not the word and.
On the front of the card, we want to include:
company logo and name (Pelton|Marsh & Quillan)
on the back, we would definitely include:
address, email, cell #
logo and name (smaller size than front)

The variable will be location of individual name and title (mine for example is ) - whether on the front OR on the back. interested in variations from which to choose
Dr. Neil R. Whitcombe, CFA
Scientifique des Fusées Financières

we would like to use contemporary symbols for address, email address, cell # with an option for web site that we do not intend to use initially. we like two sided cards and believe this design should use four rounded corners with the standard size. we prefer thicker card stock and may look at metal.

```html
<!DOCTYPE html>
<html lang="en">
<head>
<meta charset="utf-8">
<title>Pelton|Marsh &amp; Quillan — Business Card</title>
<link rel="stylesheet" href="https://fonts.googleapis.com/css2?family=Montserrat:wght@700&family=Source+Serif+4:wght@400&family=Open+Sans:wght@300&display=swap">
<style>
  :root {
    --card-bg: #ffffff;
    --ink: #111111;
    --muted: #6b6b6b;
    --brand-grey: #666666;
    --brand-orange: #d9741c;
    --edge: #3a3a3a;
  }
  html, body {
    margin: 0;
    padding: 0;
    width: 1200px;
    height: 708px;
    overflow: hidden;
    background: var(--card-bg);
  }
  .card {
    position: relative;
    width: 1200px;
    height: 708px;
    background: var(--card-bg);
    border-top: 1px solid var(--edge);
    box-sizing: border-box;
    font-family: "Source Serif 4", Georgia, serif;
    color: var(--ink);
  }
  .brand {
    position: absolute;
    top: 42px;
    left: 877px;
    width: 300px;
    display: flex;
    flex-direction: column;
    align-items: center;
  }
  .brand__mark {
    width: 80px;
    height: 80px;
    background: var(--brand-orange);
  }
  .brand__name {
    margin-top: 30px;
    font-family: "Source Serif 4", Georgia, serif;
    font-weight: 400;
    font-size: 27px;
    line-height: 1;
    letter-spacing: 0.3px;
    color: var(--brand-grey);
    white-space: nowrap;
  }
  .person {
    position: absolute;
    left: 72px;
    top: 309px;
  }
  .person__name {
    margin: 0;
    font-family: "Montserrat", Arial, sans-serif;
    font-weight: 700;
    font-size: 39px;
    line-height: 1;
    letter-spacing: 0.2px;
    color: var(--ink);
  }
  .person__role {
    margin: 16px 0 0;
    font-size: 29px;
    line-height: 1;
    letter-spacing: 1.7px;
    color: var(--muted);
  }
  .contact {
    position: absolute;
    left: 72px;
    top: 460px;
    margin: 0;
    font-size: 29.5px;
    line-height: 37.5px;
    letter-spacing: 1.5px;
    font-style: normal;
  }
  .contact__address {
    margin-top: 42px;
  }
  .website {
    position: absolute;
    left: 1156px;
    top: 676px;
    transform: rotate(-90deg);
    transform-origin: left top;
    font-family: "Open Sans", Arial, sans-serif;
    font-weight: 300;
    font-size: 27px;
    line-height: 1;
    letter-spacing: 1.4px;
    color: var(--ink);
    white-space: nowrap;
  }
</style>
</head>
<body>
  <main class="card">
    <div class="brand">
      <div class="brand__mark"></div>
      <div class="brand__name">Pelton|Marsh &amp; Quillan</div>
    </div>

    <section class="person">
      <h1 class="person__name">NAME AND SURNAME</h1>
      <p class="person__role">Occupation or position</p>
    </section>

    <address class="contact">
      <div class="contact__phone">T. ##########</div>
      <div class="contact__email">E. Emailaddress</div>
      <div class="contact__address">
        Address line 1<br>
        Adress line 2
      </div>
    </address>

    <div class="website">Www.website.com</div>
  </main>
</body>
</html>
```